Venlox - Property Management Company Listings - PSD / uncoded only

Our site simply connects property owners with property managers. I’m asking you to create 2 pages, 1 homepage and 1 page that lists of property management companies. Build with Responsive Design in mind. PSD/uncoded files only. Help us create a great site!
Example competitor sites:
http://www.everyestatehelp.example/
http://www.tendyourlots.example/
Inspired by these sites:
http://www.quorvik.example/
http://www.bespokely.example/
http://www.coinwire.example/
https://www.tripboard.example/
I've attached the logo as well as 2 picture files that you can consider using.
• Venlox Logo Colors: Yellow: HTML code: #FBC30A, RGB code: R: 251 G: 195 B: 10 Grey: HTML code: #4E4C4D, RGB code: R: 78 G: 76 B: 77
• The picture files are optional.
o One picture is of houses and neighborhood.
o The other is of a professional woman on the phone. Please do not use the professional woman as a large primary image. You can use the professional woman photo as a smaller photo and not the main photo.
• Please bring your own pictures and graphics too. Don't feel like you need to use mine.
Thank you!

```html
<!DOCTYPE html>
<html lang="en">
<head>
<meta charset="utf-8">
<title>Venlox – Find Your Local Property Manager</title>
<link rel="stylesheet" href="https://fonts.googleapis.com/css2?family=Questrial&family=Arimo:wght@400;700&family=Roboto+Condensed:wght@700&display=swap">
<style>
:root{
  --yellow:#fbc30a;
  --yellow-band:#e1b412;
  --grey:#4e4c4d;
  --tab-grey:#4a4a4a;
  --panel:rgba(40,40,40,.86);
  --dark:#333333;
  --footer:#222222;
  --footer-bottom:#191919;
  --text:#333333;
  --muted:#8a8a8a;
}
*{box-sizing:border-box;margin:0;padding:0}
html,body{width:918px;height:1200px;overflow:hidden;background:#fff}
body{position:relative;font-family:"Arimo",Arial,sans-serif;color:var(--text)}
.abs{position:absolute}

/* header */
.brand{left:106px;top:18px;display:flex;align-items:center;gap:8px;font-family:"Questrial",sans-serif;font-size:44px;color:var(--grey);line-height:1}
.brand-mark{width:14px;height:14px;background:var(--yellow)}
.nav-tab{top:47px;height:39px;border-radius:5px 5px 0 0;background:var(--tab-grey);color:#fff;font-family:"Questrial",sans-serif;font-size:13px;display:flex;align-items:center;justify-content:center}
.nav-tab.is-active{background:var(--yellow);color:var(--grey)}
.header-rule{left:0;top:86px;width:918px;height:4px;background:var(--yellow)}

/* hero */
.hero-photo{left:0;top:90px;width:918px;height:347px;background:linear-gradient(160deg,#7d7a74 0%,#5d5e55 30%,#6f7a55 55%,#55544f 80%,#6b6a66 100%)}
.search-panel{left:198px;top:183px;width:518px;height:166px;background:var(--panel);border-radius:4px}
.search-title{left:224px;top:199px;font-family:"Roboto Condensed",sans-serif;font-size:23px;color:var(--yellow);letter-spacing:.2px}
.field-label{top:239px;font-size:11.5px;color:#fff}
.field{top:259px;height:28px;background:#fff;border-radius:2px}
.select-arrow{left:456px;top:268px;font-size:10px;color:#222}
.search-btn{left:553px;top:301px;width:106px;height:33px;background:var(--yellow);border-radius:3px;font-family:"Arimo",sans-serif;font-weight:700;font-size:15px;letter-spacing:1px;color:#2a2a2a;display:flex;align-items:center;justify-content:center}

/* tagline */
.tagline-band{left:0;top:437px;width:918px;height:55px;background:var(--yellow-band);font-family:"Questrial",sans-serif;font-size:22px;color:#1f1f1f;display:flex;align-items:center;justify-content:center}
.tagline-notch{left:429px;top:492px}

/* steps */
.step{top:542px;width:210px;text-align:center}
.step-number{width:80px;height:51px;margin:0 auto;border:2px solid var(--yellow-band);border-radius:6px;font-family:"Arimo",sans-serif;font-weight:700;font-size:24px;color:var(--yellow-band);display:flex;align-items:center;justify-content:center}
.step-text{margin-top:13px;font-size:10.5px;line-height:14px;color:#3a3a3a}

/* feature */
.feature-photo{left:105px;top:725px;width:358px;height:198px;background:linear-gradient(90deg,#c9c6bd 0%,#a9a69c 40%,#3b3b3d 75%,#d6d2c8 100%)}
.feature-panel{left:467px;top:725px;width:344px;height:198px;background:var(--dark);padding:14px 13px}
.feature-title{font-family:"Questrial",sans-serif;font-size:20px;color:var(--yellow);line-height:24px}
.feature-sub{font-family:"Questrial",sans-serif;font-size:16.5px;color:#fff;line-height:20px}
.feature-body{margin-top:10px;font-size:10.2px;line-height:15.6px;color:#fff;width:282px}
.read-more{display:inline-block;margin-top:10px;padding:0 11px;height:21px;line-height:21px;background:var(--yellow);border-radius:2px;font-size:10px;color:#222}

/* footer */
.footer{left:0;top:953px;width:918px;height:222px;background:var(--footer)}
.footer-heading{top:976px;font-size:12px;font-weight:700;color:var(--yellow)}
.footer-links{top:1002px;list-style:none;font-size:8px;color:#fff;line-height:17px}
.contact-phone{left:319px;top:995px;font-size:16px;font-weight:700;color:#fff}
.contact-email{left:319px;top:1020px;font-size:8px;color:#fff}
.contact-place{left:319px;top:1041px;display:flex;gap:5px;color:#fff}
.place-city{font-size:11px;font-weight:700;line-height:12px}
.place-street{font-size:7.5px;line-height:9px;font-weight:700}
.social{top:1083px;width:16px;height:16px;border-radius:2px}
.footer-note{left:135px;top:1124px;width:380px;font-size:7.4px;line-height:13.5px;color:#6f6f6f}
.form-label{font-size:8.5px;font-weight:700;color:#fff}
.form-field{background:#fff;border:1px solid #bbb}
.send-btn{left:523px;top:1136px;width:100px;height:22px;background:var(--yellow);font-size:9.5px;font-weight:700;color:#333;display:flex;align-items:center;justify-content:center}
.footer-bottom{left:0;top:1175px;width:918px;height:25px;background:var(--footer-bottom);color:#ddd;font-size:9.5px;display:flex;align-items:center;justify-content:center}
</style>
</head>
<body>

<header>
  <div class="abs brand"><span>Venlox</span><span class="brand-mark"></span></div>
  <nav>
    <div class="abs nav-tab is-active" style="left:382px;width:84px">HOME</div>
    <div class="abs nav-tab" style="left:474px;width:224px">ARE YOU A PROPERTY MANAGER?</div>
    <div class="abs nav-tab" style="left:706px;width:105px">CONTACT US</div>
  </nav>
  <div class="abs header-rule"></div>
</header>

<section>
  <div class="abs hero-photo" role="img" aria-label="Aerial view of a suburban neighbourhood with houses, trees and parked cars"></div>
  <div class="abs search-panel"></div>
  <h1 class="abs search-title">FIND YOUR LOCAL PROPERTY MANAGER</h1>
  <div class="abs field-label" style="left:226px">Select Your Property Type</div>
  <div class="abs field-label" style="left:499px">In Zipcode</div>
  <div class="abs field" style="left:226px;width:246px"></div>
  <div class="abs select-arrow">▼</div>
  <div class="abs field" style="left:498px;width:161px"></div>
  <div class="abs search-btn">SEARCH</div>
</section>

<div class="abs tagline-band">Connecting property owners with property managers</div>
<svg class="abs tagline-notch" width="18" height="9" viewBox="0 0 18 9"><polygon points="0,0 18,0 9,9" fill="#e1b412"/></svg>

<section>
  <div class="abs step" style="left:101px"><div class="step-number">01</div><p class="step-text">If you are going to use a passage of Lorem Ipsum, you need to be sure there isnt anything embarrassing hidden in the middle of text. All the Lorem Ipsum generators on the Internet tend to repeat.</p></div>
  <div class="abs step" style="left:347px"><div class="step-number">02</div><p class="step-text">If you are going to use a passage of Lorem Ipsum, you need to be sure there isnt anything embarrassing hidden in the middle of text. All the Lorem Ipsum generators on the Internet tend to repeat.</p></div>
  <div class="abs step" style="left:595px"><div class="step-number">03</div><p class="step-text">If you are going to use a passage of Lorem Ipsum, you need to be sure there isnt anything embarrassing hidden in the middle of text. All the Lorem Ipsum generators on the Internet tend to repeat.</p></div>
</section>

<section>
  <div class="abs feature-photo" role="img" aria-label="Smiling professional woman in a dark suit talking on a phone in a bright corridor"></div>
  <div class="abs feature-panel">
    <h2 class="feature-title">Join Our Real Estate Property</h2>
    <p class="feature-sub">management company network.</p>
    <p class="feature-body">Donec vel ipsum a felis facilisis consequat. Integer nec lorem sit amet risus varius aliquam ut et urna. Cras aliquam mi posuere ullamcorper scelerisque. Vestibulum interdum vehicula feugiat. Nam&nbsp; nec lorem sit amet risus varius aliquam ut et urna. Cras aliquam mi posuere.</p>
    <span class="read-more">Read More...</span>
  </div>
</section>

<footer>
  <div class="abs footer"></div>
  <h3 class="abs footer-heading" style="left:136px">Information</h3>
  <h3 class="abs footer-heading" style="left:228px">Useful Links</h3>
  <h3 class="abs footer-heading" style="left:319px">Contacts</h3>
  <ul class="abs footer-links" style="left:136px"><li>About company</li><li>Our team</li><li>Registration</li><li>Payment Option</li><li>Infomation</li><li>FAQ</li></ul>
  <ul class="abs footer-links" style="left:227px"><li>Homepage</li><li>404 page</li><li>Grid system</li><li>Our agents</li><li>Typography</li><li>Sitemap</li></ul>
  <div class="abs contact-phone">800 555 01 47</div>
  <div class="abs contact-email">hello@venlox.example</div>
  <div class="abs contact-place">
    <svg width="6" height="9" viewBox="0 0 6 9"><path d="M3 0a3 3 0 0 0-3 3c0 2 3 6 3 6s3-4 3-6a3 3 0 0 0-3-3z" fill="#999"/><circle cx="3" cy="3" r="1.1" fill="#222"/></svg>
    <div><div class="place-city">Netherlands</div><div class="place-street">Lindengracht, KL Amsterdam 12/4</div></div>
  </div>
  <div class="abs social" style="left:319px;background:#3aa9e0"></div>
  <div class="abs social" style="left:344px;background:#3b5a9a"></div>
  <div class="abs social" style="left:369px;background:#d9412f"></div>
  <div class="abs social" style="left:394px;background:#d8221c"></div>
  <div class="abs social" style="left:418px;background:#b89a78"></div>
  <p class="abs footer-note">All the Lorem Ipsum generators on the Internet tend to repeat predefined chunks as necessary, making this the first true generator on the Internet. It uses a dictionary of over 200 Latin words, combined with a handful of model sentence structures.</p>

  <div class="abs form-label" style="left:523px;top:977px">Your name:</div>
  <div class="abs form-label" style="left:659px;top:977px">E-mail:</div>
  <div class="abs form-field" style="left:523px;top:994px;width:125px;height:29px"></div>
  <div class="abs form-field" style="left:658px;top:994px;width:126px;height:29px"></div>
  <div class="abs form-label" style="left:523px;top:1041px">Message:</div>
  <div class="abs form-field" style="left:523px;top:1058px;width:263px;height:61px"></div>
  <div class="abs send-btn">SEND MESSAGE ›</div>

  <div class="abs footer-bottom">© Copyright 2014 Venlox · All Rights Reserved. Developed</div>
</footer>

</body>
</html>
```